BrightLane Driving School

I need a Facebook page for my Driving School. I teach mostly teenagers how to drive in New Hampshire but also do private classes for adults as well. More info can be found at brightlanelessons.com

```html
<!DOCTYPE html>
<html lang="en">
<head>
<meta charset="utf-8">
<title>BrightLane Driving School – Facebook Cover</title>
<link rel="stylesheet" href="https://fonts.googleapis.com/css2?family=Montserrat:wght@500;600;800&family=Roboto:wght@700&display=swap">
<style>
  :root {
    --page-bg: #d5d8dc;
    --brand-yellow: #fcd95a;
    --label-band: rgba(252, 217, 90, 0.82);
    --ink: #111111;
    --white: #ffffff;
    --photo-senior-a: #f2b6a8;
    --photo-senior-b: #c9432f;
    --photo-middle-a: #5b6a6e;
    --photo-middle-b: #2c3436;
    --photo-teen-a: #e9d3a6;
    --photo-teen-b: #d8b64a;
  }
  html, body {
    margin: 0;
    padding: 0;
    width: 1200px;
    height: 1120px;
    overflow: hidden;
    background: var(--page-bg);
  }
  .cover-artwork {
    position: absolute;
    left: 40px;
    top: 305px;
    width: 1120px;
    height: 510px;
    display: block;
  }
  .brand-name { font-family: "Montserrat", sans-serif; font-weight: 800; fill: var(--ink); }
  .brand-phone { font-family: "Montserrat", sans-serif; font-weight: 800; fill: var(--ink); }
  .tagline { font-family: "Montserrat", sans-serif; font-weight: 500; fill: var(--ink); }
  .service-label { font-family: "Montserrat", sans-serif; font-weight: 600; fill: var(--ink); }
  .email-text { font-family: "Roboto", sans-serif; font-weight: 700; fill: var(--brand-yellow); }
  .profile-name { font-family: "Montserrat", sans-serif; font-weight: 800; fill: var(--ink); }
</style>
</head>
<body>
<svg class="cover-artwork" viewBox="0 0 1164 530" xmlns="http://www.w3.org/2000/svg">
  <defs>
    <clipPath id="cover-shape"><rect x="0" y="0" width="1164" height="430" rx="8"/></clipPath>
    <linearGradient id="senior-photo" x1="0" y1="0" x2="0" y2="1">
      <stop offset="0" stop-color="var(--photo-senior-a)"/>
      <stop offset="1" stop-color="var(--photo-senior-b)"/>
    </linearGradient>
    <linearGradient id="middle-photo" x1="0" y1="0" x2="1" y2="1">
      <stop offset="0" stop-color="var(--photo-middle-a)"/>
      <stop offset="1" stop-color="var(--photo-middle-b)"/>
    </linearGradient>
    <linearGradient id="teen-photo" x1="0" y1="0" x2="0" y2="1">
      <stop offset="0" stop-color="var(--photo-teen-a)"/>
      <stop offset="1" stop-color="var(--photo-teen-b)"/>
    </linearGradient>
  </defs>

  <g class="cover" clip-path="url(#cover-shape)">
    <rect class="cover-base" x="0" y="0" width="1164" height="430" fill="var(--brand-yellow)"/>
    <rect class="brand-panel" x="0" y="20" width="460" height="128" fill="var(--white)"/>

    <polygon class="photo-senior" role="img" aria-label="Photo of a smiling senior driver at the wheel of a red car"
             points="445,0 755,0 575,430 270,430" fill="url(#senior-photo)"/>
    <polygon class="photo-instructor" role="img" aria-label="Photo of an instructor and a teenage student seated in a car"
             points="755,0 1065,0 890,430 575,430" fill="url(#middle-photo)"/>
    <polygon class="photo-teen" role="img" aria-label="Photo of a smiling young woman in a yellow car"
             points="1065,0 1164,0 1164,430 890,430" fill="url(#teen-photo)"/>

    <line class="panel-divider" x1="755" y1="0" x2="575" y2="430" stroke="var(--brand-yellow)" stroke-width="8"/>
    <line class="panel-divider" x1="1065" y1="0" x2="890" y2="430" stroke="var(--brand-yellow)" stroke-width="8"/>

    <rect class="black-band" x="0" y="307" width="330" height="31" fill="var(--ink)"/>
    <polygon class="label-band" points="345,270 1164,270 1164,330 320,330" fill="var(--label-band)"/>

    <text class="service-label" font-size="14">
      <tspan x="455" y="295">SENIOR DRIVER</tspan>
      <tspan x="455" y="315">EVALUATIONS</tspan>
    </text>
    <text class="service-label" font-size="14">
      <tspan x="676" y="287">INDIVIDUAL</tspan>
      <tspan x="676" y="305">DRIVER</tspan>
      <tspan x="676" y="323">EDUCATION</tspan>
    </text>
    <text class="service-label" font-size="14">
      <tspan x="990" y="287">TEENAGE</tspan>
      <tspan x="990" y="305">GROUP DRIVER</tspan>
      <tspan x="990" y="323">EDUCATION</tspan>
    </text>

    <polygon class="email-bar" points="565,396 650,338 1164,338 1164,396" fill="var(--ink)"/>
    <g class="email-icon" fill="none" stroke="var(--white)" stroke-width="2.5">
      <rect x="710" y="354" width="42" height="26"/>
      <polyline points="710,354 731,370 752,354"/>
      <line x1="710" y1="380" x2="725" y2="366"/>
      <line x1="752" y1="380" x2="737" y2="366"/>
    </g>
    <text class="email-text" x="758" y="376" font-size="24">admin@brightlanelessons.com</text>

    <circle class="brand-dot" cx="44" cy="84" r="30" fill="var(--ink)"/>
    <text class="brand-name" font-size="30">
      <tspan x="90" y="76">BrightLane</tspan>
    </text>
    <text class="brand-name" font-size="19">
      <tspan x="90" y="102">Driving School</tspan>
    </text>
    <text class="brand-phone" x="90" y="128" font-size="16" letter-spacing="1">603 555 0142</text>

    <text class="tagline" x="10" y="205" font-size="18">AWARD-WINNING DRIVING SCHOOL</text>
  </g>

  <g class="profile-picture">
    <circle cx="111" cy="441" r="82" fill="var(--white)"/>
    <circle cx="111" cy="418" r="12" fill="var(--brand-yellow)"/>
    <text class="profile-name" x="111" y="452" font-size="19" text-anchor="middle">BrightLane</text>
  </g>
</svg>
</body>
</html>
```